Bewerbungs-Template
Zielgruppe
Ich bin einen Einzelperson und möchte meine Bewerbungsunterlagen überarbeiten. Meine Zielgruppe ist ein potentieller Arbeitgeber welcher überzeugen möchte.
Aufgabenstellung
Das Design sollte professionell und übersichtlich aussehen und ein bisschen einzigartig sein. Es sollte nicht nur ein Deckblatt sein, wichtig ist für mich vor allem die CV-Gestaltung. Es muss kein Word-Format sein, kann mit den gängigen Office oder Photoprogrammen erstellt werden. In meinem Kopf schwirrt eine schlichte Idee mit einem Bordeaux-Roten Highlight herum, vlt. hat jemand eine Gute Idee :)
Ich bedanke mich bereits im Voraus für alle Ideen.

```html
<!DOCTYPE html>
<html lang="de">
<head>
<meta charset="utf-8">
<title>Bewerbung – Template</title>
<link rel="stylesheet" href="https://fonts.googleapis.com/css2?family=Montserrat:wght@500;600&display=swap">
<style>
  :root {
    --bordeaux: #8b0000;
    --ink: #555555;
    --cover-grey: #e5e5e5;
    --paper: #ffffff;
    --rule: #444444;
  }
  html, body { margin: 0; padding: 0; width: 1200px; height: 5092px; overflow: hidden; background: var(--paper); }
  .sheet { display: block; width: 1200px; height: 5092px; }
  .title { font-family: "Montserrat", sans-serif; font-weight: 600; fill: var(--ink); }
  .year-label { font-family: "Montserrat", sans-serif; font-weight: 600; fill: var(--ink); font-size: 18px; }
  .placeholder { fill: var(--ink); }
  .pill { fill: var(--cover-grey); }
  .accent { fill: var(--bordeaux); }
  .page-frame { fill: none; stroke: var(--rule); stroke-width: 1; }
</style>
</head>
<body>
<svg class="sheet" viewBox="0 0 595 2525" preserveAspectRatio="none" xmlns="http://www.w3.org/2000/svg">
  <!-- Cover -->
  <rect class="cover-band" x="0" y="0" width="595" height="507" fill="var(--cover-grey)"/>
  <text class="title" x="5" y="462" font-size="100" textLength="530" lengthAdjust="spacingAndGlyphs">Bewerbung</text>
  <rect class="accent" x="437" y="506" width="158" height="10"/>
  <circle class="accent" cx="437" cy="511" r="17"/>

  <!-- Page frames -->
  <line class="page-frame" x1="0.5" y1="507" x2="0.5" y2="2525"/>
  <line class="page-frame" x1="594.5" y1="516" x2="594.5" y2="2525"/>
  <line class="page-frame" x1="0" y1="842" x2="595" y2="842"/>
  <line class="page-frame" x1="0" y1="1683.5" x2="595" y2="1683.5"/>
  <line class="page-frame" x1="0" y1="2524.5" x2="595" y2="2524.5"/>

  <!-- Cover letter -->
  <g class="placeholder letter">
    <rect x="18" y="861" width="14" height="16"/><rect x="37" y="861" width="65" height="16"/><rect x="107" y="861" width="90" height="16"/>
    <rect x="18" y="888" width="40" height="16"/><rect x="63" y="888" width="77" height="16"/>
    <rect x="18" y="915" width="27" height="16"/><rect x="50" y="915" width="77" height="16"/>
    <rect x="18" y="942" width="103" height="16"/>
    <rect x="440" y="861" width="52" height="16"/><rect x="497" y="861" width="78" height="16"/>
    <rect x="399" y="977" width="26" height="16"/><rect x="430" y="977" width="65" height="16"/><rect x="500" y="977" width="78" height="16"/>
    <rect x="469" y="1004" width="26" height="16"/><rect x="500" y="1004" width="78" height="16"/>
    <rect x="418" y="1030" width="90" height="16"/><rect x="513" y="1030" width="65" height="16"/>
    <rect x="475" y="1057" width="103" height="16"/>
    <rect x="18" y="1110" width="68" height="18"/><rect x="91" y="1110" width="69" height="18"/><rect x="166" y="1110" width="69" height="18"/><rect x="241" y="1110" width="41" height="18"/><rect x="288" y="1110" width="69" height="18"/><rect x="362" y="1110" width="137" height="18"/>
    <rect x="18" y="1167" width="136" height="16"/><rect x="159" y="1167" width="83" height="16"/><rect x="247" y="1167" width="43" height="16"/><rect x="295" y="1167" width="55" height="16"/><rect x="356" y="1167" width="82" height="16"/>
    <rect x="18" y="1196" width="82" height="16"/><rect x="105" y="1196" width="83" height="16"/><rect x="193" y="1196" width="110" height="16"/><rect x="308" y="1196" width="29" height="16"/><rect x="342" y="1196" width="84" height="16"/><rect x="431" y="1196" width="28" height="16"/>
    <rect x="18" y="1224" width="82" height="16"/><rect x="105" y="1224" width="69" height="16"/><rect x="179" y="1224" width="111" height="16"/><rect x="295" y="1224" width="69" height="16"/><rect x="369" y="1224" width="42" height="16"/><rect x="416" y="1224" width="56" height="16"/>
    <rect x="18" y="1253" width="122" height="16"/><rect x="145" y="1253" width="29" height="16"/><rect x="179" y="1253" width="56" height="16"/><rect x="240" y="1253" width="43" height="16"/><rect x="288" y="1253" width="28" height="16"/><rect x="321" y="1253" width="97" height="16"/><rect x="423" y="1253" width="29" height="16"/><rect x="457" y="1253" width="69" height="16"/>
    <rect x="18" y="1282" width="40" height="16"/><rect x="63" y="1282" width="97" height="16"/><rect x="166" y="1282" width="28" height="16"/><rect x="199" y="1282" width="29" height="16"/><rect x="233" y="1282" width="83" height="16"/><rect x="321" y="1282" width="56" height="16"/><rect x="382" y="1282" width="70" height="16"/><rect x="457" y="1282" width="55" height="16"/>
    <rect x="18" y="1310" width="136" height="16"/><rect x="159" y="1310" width="29" height="16"/><rect x="193" y="1310" width="42" height="16"/><rect x="240" y="1310" width="110" height="16"/><rect x="355" y="1310" width="97" height="16"/><rect x="457" y="1310" width="42" height="16"/>
    <rect x="18" y="1339" width="68" height="16"/><rect x="91" y="1339" width="69" height="16"/><rect x="166" y="1339" width="69" height="16"/><rect x="240" y="1339" width="42" height="16"/><rect x="288" y="1339" width="69" height="16"/><rect x="362" y="1339" width="70" height="16"/><rect x="437" y="1339" width="69" height="16"/>
    <rect x="18" y="1368" width="68" height="16"/><rect x="91" y="1368" width="42" height="16"/>
    <rect x="18" y="1396" width="68" height="16"/><rect x="91" y="1396" width="138" height="16"/><rect x="234" y="1396" width="137" height="16"/><rect x="376" y="1396" width="83" height="16"/>
    <rect x="18" y="1425" width="40" height="16"/><rect x="63" y="1425" width="57" height="16"/><rect x="125" y="1425" width="83" height="16"/><rect x="213" y="1425" width="83" height="16"/><rect x="301" y="1425" width="83" height="16"/><rect x="389" y="1425" width="110" height="16"/>
    <rect x="18" y="1453" width="27" height="16"/><rect x="50" y="1453" width="83" height="16"/><rect x="138" y="1453" width="29" height="16"/><rect x="172" y="1453" width="83" height="16"/><rect x="260" y="1453" width="70" height="16"/><rect x="335" y="1453" width="110" height="16"/>
    <rect x="18" y="1482" width="68" height="16"/><rect x="91" y="1482" width="42" height="16"/><rect x="138" y="1482" width="56" height="16"/><rect x="199" y="1482" width="124" height="16"/><rect x="328" y="1482" width="29" height="16"/><rect x="362" y="1482" width="56" height="16"/><rect x="423" y="1482" width="42" height="16"/>
    <rect x="18" y="1510" width="27" height="16"/><rect x="50" y="1510" width="96" height="16"/><rect x="152" y="1510" width="29" height="16"/><rect x="186" y="1510" width="69" height="16"/><rect x="260" y="1510" width="42" height="16"/><rect x="307" y="1510" width="97" height="16"/><rect x="409" y="1510" width="29" height="16"/><rect x="443" y="1510" width="29" height="16"/><rect x="477" y="1510" width="83" height="16"/>
    <rect x="18" y="1539" width="54" height="16"/><rect x="77" y="1539" width="70" height="16"/><rect x="152" y="1539" width="56" height="16"/>
    <rect x="18" y="1596" width="40" height="16"/><rect x="63" y="1596" width="56" height="16"/>
    <rect x="18" y="1624" width="82" height="16"/><rect x="105" y="1624" width="109" height="16"/>
  </g>

  <!-- Curriculum vitae -->
  <text class="title" x="3" y="1718" font-size="44" textLength="64" lengthAdjust="spacingAndGlyphs">CV</text>
  <polygon class="accent timeline" points="72,1684 82,1684 85,2475 75,2475"/>
  <circle class="accent" cx="80" cy="2475" r="17"/>

  <g class="cv-entry">
    <rect class="pill" x="85" y="1736" width="70" height="27" rx="13"/>
    <polygon class="pill" points="77,1749.5 86,1744 86,1755"/>
    <text class="year-label" x="97" y="1756" textLength="40" lengthAdjust="spacingAndGlyphs">2011</text>
  </g>
  <g class="cv-entry">
    <rect class="pill" x="85" y="1840" width="70" height="27" rx="13"/>
    <polygon class="pill" points="77,1853.5 86,1848 86,1859"/>
    <rect x="92" y="1845" width="55" height="17" fill="var(--ink)"/>
  </g>
  <g class="cv-entry">
    <rect class="pill" x="85" y="1942" width="70" height="27" rx="13"/>
    <polygon class="pill" points="77,1955.5 86,1950 86,1961"/>
    <rect x="92" y="1947" width="55" height="17" fill="var(--ink)"/>
  </g>
  <g class="cv-entry">
    <rect class="pill" x="85" y="2044" width="70" height="27" rx="13"/>
    <polygon class="pill" points="77,2057.5 86,2052 86,2063"/>
    <rect x="92" y="2049" width="55" height="17" fill="var(--ink)"/>
  </g>
  <g class="cv-entry">
    <rect class="pill" x="85" y="2147" width="70" height="27" rx="13"/>
    <polygon class="pill" points="77,2160.5 86,2155 86,2166"/>
    <rect x="92" y="2152" width="55" height="17" fill="var(--ink)"/>
  </g>

  <defs>
    <g id="cv-description" fill="#555555">
      <rect x="180" y="0" width="41" height="16"/><rect x="227" y="0" width="42" height="16"/><rect x="275" y="0" width="95" height="16"/><rect x="376" y="0" width="55" height="16"/><rect x="437" y="0" width="69" height="16"/><rect x="512" y="0" width="14" height="16"/><rect x="532" y="0" width="28" height="16"/>
      <rect x="180" y="28" width="28" height="16"/><rect x="214" y="28" width="55" height="16"/><rect x="275" y="28" width="55" height="16"/><rect x="336" y="28" width="55" height="16"/><rect x="397" y="28" width="28" height="16"/><rect x="431" y="28" width="68" height="16"/>
      <rect x="180" y="57" width="55" height="16"/><rect x="241" y="57" width="69" height="16"/>
    </g>
  </defs>
  <g class="placeholder cv-text" fill="#555555">
    <use href="#cv-description" y="1741"/>
    <use href="#cv-description" y="1844"/>
    <use href="#cv-description" y="1947"/>
    <use href="#cv-description" y="2049"/>
    <use href="#cv-description" y="2152"/>
  </g>

  <g class="more-indicator" fill="var(--ink)">
    <circle cx="310" cy="2293" r="9"/>
    <circle cx="331" cy="2293" r="9"/>
    <circle cx="352" cy="2293" r="9"/>
  </g>
</svg>
</body>
</html>
```